SOLVEN TRIDE PORTAL

I'D LIKE TO REDESIGN MY WEBSITE TO MATCH WITH THE NEW BROCHURE WHICH IS ATTACHED. CONTENT AND LOGOS ARE ATTACHED. PLEASE USE WATCH BRAND LOGOS FROM THE BROCHURE
Coded - Design and coding required
1 page

```html
<!DOCTYPE html>
<html lang="en">
<head>
<meta charset="utf-8">
<title>Solven Tride Portal – Home Page Samples</title>
<link rel="stylesheet" href="https://fonts.googleapis.com/css2?family=Josefin+Sans:wght@300;400&family=Cormorant+Garamond:wght@400;500&display=swap">
<style>
:root{
  --board:#b3b3b3;
  --black:#050505;
  --charcoal:#222222;
  --deep:#1a1a1a;
  --gold:#cfa93f;
  --gold-light:#f1d77c;
  --gold-dark:#a9801f;
  --white:#ffffff;
  --ink:#1b1b1b;
  --muted:#bdbdbd;
  --line:#6d5a22;
  --field:#2a2a2a;
}
*{margin:0;padding:0;box-sizing:border-box}
html,body{width:799px;height:1200px;overflow:hidden;background:var(--board)}
.board{position:relative;width:1568px;height:2355px;transform:scale(0.50957);transform-origin:0 0;background:var(--board);font-family:"Cormorant Garamond",serif}
.a{position:absolute}
.sample-title{position:absolute;font-family:"Josefin Sans",sans-serif;font-weight:300;font-size:22px;color:#1e1e1e;letter-spacing:.5px}
.page{position:absolute;width:488px;overflow:hidden;background:var(--black)}
.section{position:absolute;left:0;width:488px;overflow:hidden}
.bg-black{background:var(--black)}
.bg-white{background:var(--white)}
.bg-charcoal{background:var(--charcoal)}
.bg-deep{background:var(--deep)}
.gold-band{position:absolute;left:0;width:488px;background:linear-gradient(90deg,var(--gold-dark),var(--gold-light) 30%,var(--gold) 55%,var(--gold-light) 80%,var(--gold-dark));clip-path:polygon(0 30%,8% 10%,20% 25%,35% 0,50% 20%,64% 5%,78% 22%,90% 8%,100% 20%,100% 80%,88% 95%,72% 75%,58% 100%,42% 82%,27% 96%,12% 78%,0 92%)}
.logo-mark{position:absolute;width:46px;height:28px;border:1.5px solid var(--gold)}
.logo-name{position:absolute;font-family:"Josefin Sans",sans-serif;font-size:5.2px;color:var(--white);white-space:nowrap;letter-spacing:.2px}
.logo-tag{position:absolute;font-family:"Josefin Sans",sans-serif;font-size:2.6px;color:var(--gold);white-space:nowrap;letter-spacing:.3px}
.top-contact{position:absolute;font-family:"Josefin Sans",sans-serif;font-size:6.4px;color:var(--gold);white-space:nowrap;display:flex;align-items:center;gap:5px}
.icon{width:10px;height:10px;display:block}
.nav{position:absolute;top:40px;left:174px;display:flex;gap:0;font-family:"Josefin Sans",sans-serif;font-size:5.8px;color:var(--white);white-space:nowrap}
.nav span{margin-right:19px}
.nav .active{color:var(--gold)}
.photo{position:absolute}
.hero-title{position:absolute;left:61px;font-family:"Josefin Sans",sans-serif;font-weight:300;font-size:17px;color:var(--white);white-space:nowrap;line-height:23px}
.hero-sub{position:absolute;left:62px;font-family:"Cormorant Garamond",serif;font-size:10px;color:var(--gold);white-space:nowrap}
.body-copy{position:absolute;font-family:"Cormorant Garamond",serif;font-size:6.2px;line-height:9.5px;color:var(--white)}
.about-heading{position:absolute;left:256px;font-family:"Josefin Sans",sans-serif;font-weight:300;font-size:16px;line-height:23px;color:var(--gold);white-space:nowrap}
.about-copy{position:absolute;left:252px;top:446px;width:196px;height:140px;overflow:hidden;font-size:4.9px;line-height:8.6px}
.about-copy p{margin-bottom:8.6px}
.on-white{color:#444}
.on-dark{color:#d6d6d6}
.frame{position:absolute;border:4px solid var(--gold)}
.section-title{position:absolute;left:0;width:488px;text-align:center;font-family:"Josefin Sans",sans-serif;font-weight:300;color:var(--gold);white-space:nowrap}
.brands-title{font-size:15px;letter-spacing:5px}
.brand{position:absolute;width:87px;height:54px;border:1px solid var(--line);display:flex;align-items:center;justify-content:center;font-family:"Josefin Sans",sans-serif;font-size:9px;color:#c9c9c9;letter-spacing:1px;text-align:center}
.chev{position:absolute;width:10px;height:16px}
.invest-heading{position:absolute;left:47px;font-family:"Josefin Sans",sans-serif;font-weight:300;font-size:20px;white-space:nowrap}
.invest-copy{position:absolute;left:47px;width:205px;font-family:"Cormorant Garamond",serif;font-size:10px;line-height:12px}
.invest-copy p{margin-bottom:11px}
.form-note{font-size:7px;color:var(--white);font-family:"Cormorant Garamond",serif}
.source-title{font-size:19px}
.label{position:absolute;font-size:6px;color:var(--white);white-space:nowrap}
.select{position:absolute;height:15px;border:1px solid #8a8a8a;font-size:3.6px;color:#cfcfcf;padding:5px 0 0 4px}
.select::after{content:"";position:absolute;right:5px;top:4px;width:3px;height:3px;border-right:1px solid #cfcfcf;border-bottom:1px solid #cfcfcf;transform:rotate(45deg)}
.textarea{position:absolute;width:180px;height:55px;border:1px solid #8a8a8a}
.btn{position:absolute;height:15px;border-radius:8px;background:linear-gradient(90deg,var(--gold-dark),var(--gold-light),var(--gold));font-family:"Josefin Sans",sans-serif;font-size:5px;color:#2a2006;display:flex;align-items:center;justify-content:center;white-space:nowrap}
.products-title{color:var(--ink);font-size:20px}
.card{position:absolute;top:1607px;width:94px;height:150px;border:1px solid #e6e6e6;background:var(--white)}
.card .photo{left:14px;top:8px;width:66px;height:86px;border-radius:30px}
.card-name{position:absolute;top:108px;width:94px;text-align:center;font-size:9px;color:#333}
.card .btn{top:124px;left:24px;width:46px;height:11px;font-size:4px}
.contact-title{position:absolute;left:190px;font-family:"Josefin Sans",sans-serif;font-weight:300;font-size:17px;color:var(--gold);white-space:nowrap}
.address-title{position:absolute;left:63px;font-family:"Josefin Sans",sans-serif;font-weight:300;font-size:10px;color:var(--gold)}
.address-row{position:absolute;left:63px;display:flex;gap:8px}
.address-row .icon{width:13px;height:13px}
.address-text{font-size:5.6px;line-height:6.5px;color:var(--white)}
.address-text span{color:var(--gold);display:block}
.follow{position:absolute;left:61px;font-size:5.6px;color:var(--gold);display:flex;align-items:center;gap:4px}
.follow i{display:block;width:6px;height:6px;border:1px solid var(--white)}
.field{position:absolute;height:18px;background:var(--field);font-size:4.2px;color:#cfcfcf;padding:6px 0 0 8px}
.footer{position:absolute;left:0;width:488px;text-align:center;font-size:5.4px;color:#cfcfcf}
</style>
</head>
<body>
<div class="board">

  <div class="sample-title" style="left:326px;top:132px">HOME PAGE SAMPLE1</div>
  <div class="sample-title" style="left:957px;top:124px">HOME PAGE SAMPLE2</div>

  <!-- SAMPLE 1 -->
  <div class="page" style="left:169px;top:195px;height:2082px">
    <header class="section bg-black" style="top:0;height:55px">
      <div class="logo-mark" style="left:67px;top:12px"></div>
      <div class="logo-name" style="left:60px;top:45px">SOLVEN TRIDE PORTAL</div>
      <div class="logo-tag" style="left:64px;top:51px">LUXURY WATCH SUPPLIER</div>
      <div class="top-contact" style="left:212px;top:15px">
        <svg class="icon" viewBox="0 0 12 12"><rect x=".5" y=".5" width="11" height="11" fill="none" stroke="#cfa93f"/><path d="M4 3h1.2l.6 1.6-.8.6a5 5 0 0 0 1.8 1.8l.6-.8 1.6.6V8a1 1 0 0 1-1 1A5 5 0 0 1 3 4a1 1 0 0 1 1-1z" fill="#cfa93f"/></svg>Phone: 01615550142</div>
      <div class="top-contact" style="left:305px;top:15px">
        <svg class="icon" viewBox="0 0 12 12"><rect x=".5" y=".5" width="11" height="11" fill="none" stroke="#cfa93f"/><rect x="3" y="4" width="6" height="4.5" fill="#cfa93f"/><path d="M3 4l3 2.5L9 4" fill="none" stroke="#050505" stroke-width=".6"/></svg>sales@solventride.co.uk</div>
      <nav class="nav"><span class="active">HOME</span><span>ABOUT</span><span>INVESTMENTS</span><span>SEARCH WATCHES</span><span>CONTACT</span></nav>
    </header>
    <section class="section bg-black" style="top:55px;height:275px">
      <div class="photo" role="img" aria-label="Man in a dark suit fastening a luxury wristwatch" style="left:200px;top:0;width:288px;height:275px;background:radial-gradient(ellipse at 55% 40%,#6b5a50 0%,#2a2724 35%,#121620 70%,#080808 100%)"></div>
      <div class="hero-title" style="top:48px">WELCOME TO<br>SOLVEN TRIDE PORTAL</div>
      <div class="hero-sub" style="top:94px">International luxury timepiece supplier</div>
      <div class="body-copy" style="left:61px;top:112px;width:178px">Simply choose a desired product and allow us to source it for you at the best price and with suitable delivery terms. You will have an option to either collect your purchase from our Cheshire based boutique store, collection points are also in New York City or Dubai or get it delivered to your door via one of our fully insured couriers.<br><br>Making your luxury shopping experience as simple as it can be.</div>
    </section>
    <div class="gold-band" style="top:323px;height:17px"></div>
    <section class="section bg-white" style="top:340px;height:305px">
      <div class="frame" style="left:57px;top:80px;width:168px;height:165px"></div>
      <div class="photo" role="img" aria-label="Steel diver watch with black dial and brown leather strap" style="left:88px;top:30px;width:118px;height:208px;border-radius:40px;background:radial-gradient(ellipse at 50% 50%,#2a2a2a 0%,#6d6d6d 38%,#4a3a30 55%,#e8e8e8 80%,#ffffff 100%)"></div>
    </section>
    <div class="about-heading" style="top:383px">ABOUT<br><span style="letter-spacing:3px">SOLVEN TRIDE</span></div>
    <div class="body-copy about-copy on-white">
      <p>Solven Tride Portal was first founded in 2018, it has been established as the premier resource to buy and sell premium pre-owned watches. With thousands of watches available from brands including Corvane, Aubrel Vance, Halden Pierre, Rennard Mott, Ostera, Castien and more, plus international locations and clients there's no better place to find a luxury timepiece.</p>
      <p>Outstanding customer service is a mainstay of the Solven Tride ethos. Watch collectors are discerning shoppers, and will accept nothing but the best, which is why customer service has and always will be such an important part of the business.</p>
      <p>Our dedicated team of swiss watch experts are perfectly placed to adapt to the ever changing market conditions, giving our investors an 'out of the box' solution. Longevity is as much a focus as immediate success, ensuring you have the best options we can provide tomorrow as well as</p>
    </div>
    <section class="section bg-black" style="top:645px;height:285px">
      <div class="section-title brands-title" style="top:63px">BEST WATCH BRAND TO INVEST IN</div>
      <svg class="chev" style="left:34px;top:152px" viewBox="0 0 10 16"><path d="M8 1L2 8l6 7" fill="none" stroke="#9a9a9a" stroke-width="1.5"/></svg>
      <svg class="chev" style="left:443px;top:152px" viewBox="0 0 10 16"><path d="M2 1l6 7-6 7" fill="none" stroke="#9a9a9a" stroke-width="1.5"/></svg>
      <div class="brand" style="left:61px;top:109px">CORVANE</div>
      <div class="brand" style="left:154px;top:109px">HALDEN PIERRE</div>
      <div class="brand" style="left:247px;top:109px">OSTERA</div>
      <div class="brand" style="left:340px;top:109px">LUMIVEX</div>
      <div class="brand" style="left:61px;top:170px">TAVORIN</div>
      <div class="brand" style="left:154px;top:170px">KESTREL HAUS</div>
      <div class="brand" style="left:247px;top:170px">RIVANE</div>
      <div class="brand" style="left:340px;top:170px">BRELUND</div>
    </section>
    <section class="section bg-white" style="top:930px;height:255px">
      <svg class="a" style="left:0;top:0" width="488" height="255"><path d="M210 0L290 255M330 0L488 180M250 255L488 90M380 0L300 255" stroke="#e4e4e4" fill="none"/></svg>
      <div class="invest-heading" style="top:75px;color:var(--ink)">INVESTMENTS</div>
      <div class="invest-copy" style="top:110px;color:#333"><p>Interested in becoming part of the ever growing Solven Tride Portal?</p><p>Please leave your details contact form below and one of the team will be in touch to discuss potential options.</p></div>
      <div class="photo" role="img" aria-label="Rose gold watch with green dial and fluted bezel" style="left:282px;top:35px;width:140px;height:220px;border-radius:50px;background:radial-gradient(circle at 50% 45%,#5b7a4a 0%,#6d8a55 22%,#c98e72 32%,#e7b9a0 60%,#f7e2d6 85%)"></div>
    </section>
    <section class="section bg-black" style="top:1185px;height:315px">
      <div class="section-title form-note" style="top:27px">Fill Form with:</div>
      <div class="section-title source-title" style="top:40px">SOURCING YOUR WATCH</div>
      <div class="photo" role="img" aria-label="Black chronograph watch with rose gold accents" style="left:290px;top:85px;width:175px;height:215px;background:radial-gradient(circle at 50% 42%,#4a3a3a 0%,#2a2324 30%,#111 60%,#050505 100%)"></div>
      <div class="label" style="left:61px;top:90px">Watch brand</div>
      <div class="select" style="left:61px;top:98px;width:180px">Corvane</div>
      <div class="label" style="left:61px;top:124px">Year</div>
      <div class="label" style="left:153px;top:124px">Material</div>
      <div class="select" style="left:61px;top:133px;width:88px">2021-2022</div>
      <div class="select" style="left:153px;top:133px;width:88px">Material Name</div>
      <div class="label" style="left:61px;top:160px">Bezel</div>
      <div class="label" style="left:153px;top:160px">Strap</div>
      <div class="select" style="left:61px;top:169px;width:88px">Type</div>
      <div class="select" style="left:153px;top:169px;width:88px">Type</div>
      <div class="label" style="left:61px;top:194px">Description</div>
      <div class="textarea" style="left:61px;top:203px"></div>
      <div class="btn" style="left:118px;top:250px;width:54px">SUBMIT NOW</div>
    </section>
    <section class="section bg-white" style="top:1500px;height:320px">
      <svg class="a" style="left:0;top:0" width="488" height="320"><path d="M120 0L40 320M300 0L330 320M0 200L250 320M488 60L330 320" stroke="#ececec" fill="none"/></svg>
      <div class="section-title products-title" style="top:55px">OUR PRODUCTS</div>
      <svg class="chev" style="left:18px;top:156px" viewBox="0 0 10 16"><path d="M8 1L2 8l6 7" fill="none" stroke="#aaa" stroke-width="1.5"/></svg>
      <svg class="chev" style="left:462px;top:156px" viewBox="0 0 10 16"><path d="M2 1l6 7-6 7" fill="none" stroke="#aaa" stroke-width="1.5"/></svg>
    </section>
    <div class="card" style="left:42px"><div class="photo" role="img" aria-label="Steel sports watch with blue dial and strap" style="background:linear-gradient(#2d3f66,#b8c0cc 50%,#2d3f66)"></div><div class="card-name">Product Name</div><div class="btn">VIEW DETAILS</div></div>
    <div class="card" style="left:146px"><div class="photo" role="img" aria-label="Steel watch with silver dial and bracelet" style="background:linear-gradient(#9a9a9a,#e0e0e0 50%,#8c8c8c)"></div><div class="card-name">Product Name</div><div class="btn">VIEW DETAILS</div></div>
    <div class="card" style="left:250px"><div class="photo" role="img" aria-label="Square watch with blue dial and dark strap" style="background:linear-gradient(#1d2330,#2f5470 50%,#1d2330)"></div><div class="card-name">Product Name</div><div class="btn">VIEW DETAILS</div></div>
    <div class="card" style="left:355px"><div class="photo" role="img" aria-label="Steel diver watch with black bezel and bracelet" style="background:linear-gradient(#bdbdbd,#2a2a2a 50%,#c6c6c6)"></div><div class="card-name">Product Name</div><div class="btn">VIEW DETAILS</div></div>
    <div class="gold-band" style="top:1813px;height:20px"></div>
    <section class="section bg-black" style="top:1833px;height:249px">
      <div class="photo" role="img" aria-label="Faint world map backdrop" style="left:0;top:20px;width:488px;height:229px;background:radial-gradient(ellipse at 50% 50%,#151515 0%,#080808 70%)"></div>
      <div class="contact-title" style="top:44px">CONTACT</div>
      <div class="address-title" style="top:63px">ADDRESS</div>
      <div class="address-row" style="top:84px"><svg class="icon" viewBox="0 0 12 12"><rect x=".5" y=".5" width="11" height="11" fill="none" stroke="#cfa93f"/><path d="M4 3h1.2l.6 1.6-.8.6a5 5 0 0 0 1.8 1.8l.6-.8 1.6.6V8a1 1 0 0 1-1 1A5 5 0 0 1 3 4a1 1 0 0 1 1-1z" fill="#cfa93f"/></svg><div class="address-text">Phone:<span>01615550142</span></div></div>
      <div class="address-row" style="top:109px"><svg class="icon" viewBox="0 0 12 12"><rect x=".5" y=".5" width="11" height="11" fill="none" stroke="#cfa93f"/><rect x="3" y="4" width="6" height="4.5" fill="#cfa93f"/><path d="M3 4l3 2.5L9 4" fill="none" stroke="#050505" stroke-width=".6"/></svg><div class="address-text">Email:<span>sales@solventride.co.uk</span></div></div>
      <div class="address-row" style="top:135px"><svg class="icon" viewBox="0 0 12 12"><rect x=".5" y=".5" width="11" height="11" fill="none" stroke="#cfa93f"/><path d="M6 2.5a2.3 2.3 0 0 1 2.3 2.3C8.3 6.5 6 9.5 6 9.5S3.7 6.5 3.7 4.8A2.3 2.3 0 0 1 6 2.5z" fill="#cfa93f"/><circle cx="6" cy="4.8" r=".8" fill="#050505"/></svg><div class="address-text">Address:<span>Lorem ispudm dummy<br>ukey lorem</span></div></div>
      <div class="follow" style="top:166px">Follow us online <i></i></div>
      <div class="field" style="left:189px;top:75px;width:119px">First Name</div>
      <div class="field" style="left:314px;top:75px;width:119px">Last Name</div>
      <div class="field" style="left:189px;top:99px;width:119px">Phone Number</div>
      <div class="field" style="left:314px;top:99px;width:119px">Email</div>
      <div class="field" style="left:189px;top:123px;width:244px;height:42px">Message</div>
      <div class="btn" style="left:189px;top:178px;width:55px">SUBMIT NOW</div>
      <div class="footer" style="top:213px">© 2022 Solven Tride Portal. All Rights Reserved. &nbsp; Terms &amp; Conditions &nbsp; Privacy Policy</div>
    </section>
  </div>

  <!-- SAMPLE 2 -->
  <div class="page" style="left:806px;top:190px;height:1797px">
    <header class="section bg-black" style="top:0;height:55px">
      <div class="logo-mark" style="left:67px;top:12px"></div>
      <div class="logo-name" style="left:60px;top:45px">SOLVEN TRIDE PORTAL</div>
      <div class="logo-tag" style="left:64px;top:51px">LUXURY WATCH SUPPLIER</div>
      <div class="top-contact" style="left:212px;top:15px">
        <svg class="icon" viewBox="0 0 12 12"><rect x=".5" y=".5" width="11" height="11" fill="none" stroke="#cfa93f"/><path d="M4 3h1.2l.6 1.6-.8.6a5 5 0 0 0 1.8 1.8l.6-.8 1.6.6V8a1 1 0 0 1-1 1A5 5 0 0 1 3 4a1 1 0 0 1 1-1z" fill="#cfa93f"/></svg>Phone: 01615550142</div>
      <div class="top-contact" style="left:305px;top:15px">
        <svg class="icon" viewBox="0 0 12 12"><rect x=".5" y=".5" width="11" height="11" fill="none" stroke="#cfa93f"/><rect x="3" y="4" width="6" height="4.5" fill="#cfa93f"/><path d="M3 4l3 2.5L9 4" fill="none" stroke="#050505" stroke-width=".6"/></svg>sales@solventride.co.uk</div>
      <nav class="nav"><span class="active">HOME</span><span>ABOUT</span><span>INVESTMENTS</span><span>SEARCH WATCHES</span><span>CONTACT</span></nav>
    </header>
    <section class="section bg-black" style="top:55px;height:275px">
      <div class="photo" role="img" aria-label="Man in a dark suit fastening a luxury wristwatch" style="left:200px;top:0;width:288px;height:275px;background:radial-gradient(ellipse at 55% 40%,#6b5a50 0%,#2a2724 35%,#121620 70%,#080808 100%)"></div>
      <div class="hero-title" style="top:48px">WELCOME TO<br>SOLVEN TRIDE PORTAL</div>
      <div class="hero-sub" style="top:94px">International luxury timepiece supplier</div>
      <div class="body-copy" style="left:61px;top:112px;width:178px">Simply choose a desired product and allow us to source it for you at the best price and with suitable delivery terms. You will have an option to either collect your purchase from our Cheshire based boutique store, collection points are also in New York City or Dubai or get it delivered to your door via one of our fully insured couriers.<br><br>Making your luxury shopping experience as simple as it can be.</div>
    </section>
    <div class="gold-band" style="top:323px;height:17px"></div>
    <section class="section bg-charcoal" style="top:340px;height:305px">
      <div class="frame" style="left:57px;top:80px;width:168px;height:165px"></div>
      <div class="photo" role="img" aria-label="Steel diver watch with black dial and brown leather strap" style="left:88px;top:30px;width:118px;height:208px;border-radius:40px;background:radial-gradient(ellipse at 50% 50%,#1a1a1a 0%,#5d5d5d 38%,#3f3128 60%,#222 100%)"></div>
    </section>
    <div class="about-heading" style="top:383px">ABOUT<br>SOLVEN TRIDE</div>
    <div class="body-copy about-copy on-dark">
      <p>Solven Tride Portal was first founded in 2018, it has been established as the premier resource to buy and sell premium pre-owned watches. With thousands of watches available from brands including Corvane, Aubrel Vance, Halden Pierre, Rennard Mott, Ostera, Castien and more, plus international locations and clients there's no better place to find a luxury timepiece.</p>
      <p>Outstanding customer service is a mainstay of the Solven Tride ethos. Watch collectors are discerning shoppers, and will accept nothing but the best, which is why customer service has and always will be such an important part of the business.</p>
      <p>Our dedicated team of swiss watch experts are perfectly placed to adapt to the ever changing market conditions, giving our investors an 'out of the box' solution. Longevity is as much a focus as immediate success, ensuring you have the best options we can provide tomorrow as well as</p>
    </div>
    <section class="section bg-black" style="top:645px;height:270px">
      <svg class="a" style="left:0;top:0" width="488" height="270"><path d="M210 0L290 270M330 0L488 180M250 270L488 90M380 0L300 270" stroke="#1e1e1e" fill="none"/></svg>
      <div class="invest-heading" style="top:68px;color:var(--gold)">INVESTMENTS</div>
      <div class="invest-copy" style="top:103px;color:var(--white)"><p>Interested in becoming part of the ever growing Solven Tride Portal?</p><p>Please leave your details contact form below and one of the team will be in touch to discuss potential options.</p></div>
      <div class="photo" role="img" aria-label="Rose gold watch with green dial and fluted bezel" style="left:282px;top:40px;width:140px;height:230px;border-radius:50px;background:radial-gradient(circle at 50% 45%,#5b7a4a 0%,#6d8a55 22%,#c98e72 32%,#e7b9a0 60%,#2a201c 100%)"></div>
    </section>
    <section class="section bg-deep" style="top:915px;height:320px">
      <div class="section-title form-note" style="top:37px">Fill Form with:</div>
      <div class="section-title source-title" style="top:50px">SOURCING YOUR WATCH</div>
      <div class="photo" role="img" aria-label="Seated man in a brown jacket wearing a wristwatch" style="left:0;top:70px;width:260px;height:250px;background:radial-gradient(ellipse at 50% 45%,#5a4032 0%,#3a2b22 35%,#1f1f22 70%,#1a1a1a 100%)"></div>
      <div class="label" style="left:243px;top:93px">Watch brand</div>
      <div class="select" style="left:243px;top:101px;width:180px">Corvane</div>
      <div class="label" style="left:243px;top:128px">Year</div>
      <div class="label" style="left:335px;top:128px">Material</div>
      <div class="select" style="left:243px;top:137px;width:88px">2021-2022</div>
      <div class="select" style="left:335px;top:137px;width:88px">Material Name</div>
      <div class="label" style="left:243px;top:163px">Bezel</div>
      <div class="label" style="left:335px;top:163px">Strap</div>
      <div class="select" style="left:243px;top:172px;width:88px">Type</div>
      <div class="select" style="left:335px;top:172px;width:88px">Type</div>
      <div class="label" style="left:243px;top:197px">Description</div>
      <div class="textarea" style="left:243px;top:207px"></div>
      <div class="btn" style="left:300px;top:253px;width:54px">SUBMIT NOW</div>
    </section>
    <section class="section bg-black" style="top:1235px;height:295px">
      <div class="section-title brands-title" style="top:72px">BEST WATCH BRAND TO INVEST IN</div>
      <svg class="chev" style="left:34px;top:162px" viewBox="0 0 10 16"><path d="M8 1L2 8l6 7" fill="none" stroke="#9a9a9a" stroke-width="1.5"/></svg>
      <svg class="chev" style="left:443px;top:162px" viewBox="0 0 10 16"><path d="M2 1l6 7-6 7" fill="none" stroke="#9a9a9a" stroke-width="1.5"/></svg>
      <div class="brand" style="left:61px;top:115px">CORVANE</div>
      <div class="brand" style="left:154px;top:115px">HALDEN PIERRE</div>
      <div class="brand" style="left:247px;top:115px">OSTERA</div>
      <div class="brand" style="left:340px;top:115px">LUMIVEX</div>
      <div class="brand" style="left:61px;top:176px">TAVORIN</div>
      <div class="brand" style="left:154px;top:176px">KESTREL HAUS</div>
      <div class="brand" style="left:247px;top:176px">RIVANE</div>
      <div class="brand" style="left:340px;top:176px">BRELUND</div>
    </section>
    <div class="gold-band" style="top:1530px;height:20px"></div>
    <section class="section bg-black" style="top:1550px;height:247px">
      <div class="photo" role="img" aria-label="Faint world map backdrop" style="left:0;top:20px;width:488px;height:227px;background:radial-gradient(ellipse at 50% 50%,#151515 0%,#080808 70%)"></div>
      <div class="contact-title" style="top:45px">CONTACT</div>
      <div class="address-title" style="top:67px">ADDRESS</div>
      <div class="address-row" style="top:87px"><svg class="icon" viewBox="0 0 12 12"><rect x=".5" y=".5" width="11" height="11" fill="none" stroke="#cfa93f"/><path d="M4 3h1.2l.6 1.6-.8.6a5 5 0 0 0 1.8 1.8l.6-.8 1.6.6V8a1 1 0 0 1-1 1A5 5 0 0 1 3 4a1 1 0 0 1 1-1z" fill="#cfa93f"/></svg><div class="address-text">Phone:<span>01615550142</span></div></div>
      <div class="address-row" style="top:112px"><svg class="icon" viewBox="0 0 12 12"><rect x=".5" y=".5" width="11" height="11" fill="none" stroke="#cfa93f"/><rect x="3" y="4" width="6" height="4.5" fill="#cfa93f"/><path d="M3 4l3 2.5L9 4" fill="none" stroke="#050505" stroke-width=".6"/></svg><div class="address-text">Email:<span>sales@solventride.co.uk</span></div></div>
      <div class="address-row" style="top:138px"><svg class="icon" viewBox="0 0 12 12"><rect x=".5" y=".5" width="11" height="11" fill="none" stroke="#cfa93f"/><path d="M6 2.5a2.3 2.3 0 0 1 2.3 2.3C8.3 6.5 6 9.5 6 9.5S3.7 6.5 3.7 4.8A2.3 2.3 0 0 1 6 2.5z" fill="#cfa93f"/><circle cx="6" cy="4.8" r=".8" fill="#050505"/></svg><div class="address-text">Address:<span>Lorem ispudm dummy<br>ukey lorem</span></div></div>
      <div class="follow" style="top:170px">Follow us online <i></i></div>
      <div class="field" style="left:189px;top:78px;width:119px">First Name</div>
      <div class="field" style="left:314px;top:78px;width:119px">Last Name</div>
      <div class="field" style="left:189px;top:103px;width:119px">Phone Number</div>
      <div class="field" style="left:314px;top:103px;width:119px">Email</div>
      <div class="field" style="left:189px;top:127px;width:244px;height:40px">Message</div>
      <div class="btn" style="left:189px;top:176px;width:55px">SUBMIT NOW</div>
      <div class="footer" style="top:214px">© 2022 Solven Tride Portal. All Rights Reserved. &nbsp; Terms &amp; Conditions &nbsp; Privacy Policy</div>
    </section>
  </div>

</div>
</body>
</html>
```